Baby Organic Coconut Body Lotion

Pebble Lane Naturals is developing a line of Organic and Natural skin care products for babies and toddlers, although our skin care can also be used by adults too. These products include a body lotion, shampoo & body wash, powder, hair cream, massage body oil, bath soak, baby balm, Bar Soap, gift box and many more.
This will be an ever expanding line so the list will go on and on. We are looking forward for an eye catching designs. I attached some of our current label designs and product images. Also, we have different Baby organic body lotion and Baby organic shampoo & body wash with different fruit flavours. Coconut lotion will share the same design with the shampoo & body wash. I would like you to start with the coconut design. I have uploaded plastic bottles with different colourful caps. The bottle with the white cap is for the coconut design. the bottle with the red cap is for the strawberry design. the bottle with the orange cap is for the orange design. the bottle with the yellow cap is for the pineapple design. the bottle with the green cap is for the apple design. Bear in my mind that my baby organic skin care are made with different fruit flavours.
Target Market(s)
My target market are for mothers that wants to buy there baby and toddler skin care products.
Industry/Entity Type
Baby
Look and feel

```html
<!DOCTYPE html>
<html lang="en">
<head>
<meta charset="utf-8">
<title>Pebble Lane Naturals – Baby Organic Coconut Body Lotion</title>
<link href="https://fonts.googleapis.com/css2?family=Arimo:wght@400;700&family=Dancing+Script:wght@500;600&family=Neucha&display=swap" rel="stylesheet">
<style>
  :root {
    --sand: #e0c3b2;
    --peach-edge: #fbe6d9;
    --peach-soft: #fdf1e8;
    --white: #ffffff;
    --brand-teal: #1fa9b7;
    --sky: #29a9e0;
    --rose: #ec6fa8;
    --cocoa: #5a3a1e;
    --rule: #6b4a33;
    --ink: #111111;
  }
  * { margin: 0; padding: 0; box-sizing: border-box; }
  html, body { width: 900px; height: 1200px; overflow: hidden; background: var(--white); }
  .label { position: relative; width: 900px; height: 1200px; background: var(--white); }

  .front-panel { position: absolute; left: 0; top: 0; width: 556px; height: 1200px; background: var(--sand); }
  .front-card {
    position: absolute; left: 72px; top: 72px; width: 416px; height: 1052px;
    background: var(--peach-edge);
  }
  .front-inner {
    position: absolute; left: 6px; top: 6px; right: 6px; bottom: 6px;
    background: var(--white);
    box-shadow: 0 0 10px 4px var(--peach-soft) inset;
  }

  .brand { position: absolute; left: 20px; right: 20px; top: 40px; height: 160px;
    display: flex; align-items: center; justify-content: center; gap: 14px; }
  .brand-dot { width: 26px; height: 26px; border-radius: 50%; background: var(--rose); flex: none; }
  .brand-name { font-family: "Arimo", Arial, sans-serif; font-weight: 700; font-size: 38px;
    line-height: 1.1; color: var(--brand-teal); }

  .brand-rule { position: absolute; left: 26px; right: 26px; top: 204px; height: 2px; background: var(--rule); }
  .tagline { position: absolute; left: 0; right: 0; top: 212px; text-align: center;
    font-family: "Arimo", Arial, sans-serif; font-size: 27px; line-height: 35px; color: var(--sky); }

  .range { position: absolute; left: 0; right: 0; top: 342px; text-align: center;
    font-family: "Dancing Script", cursive; font-weight: 500; font-size: 42px; color: var(--rose); }
  .flavour-band { position: absolute; left: -6px; right: -6px; top: 414px; height: 62px;
    background: linear-gradient(90deg, var(--peach-soft), #fff8f2 35%, #fff8f2 65%, var(--peach-soft)); }
  .flavour { position: absolute; left: 0; right: 0; top: 408px; text-align: center;
    font-family: "Neucha", cursive; font-size: 60px; color: var(--cocoa); }
  .product { position: absolute; left: 0; right: 0; top: 480px; text-align: center;
    font-family: "Dancing Script", cursive; font-weight: 600; font-size: 70px; color: var(--rose); }

  .fruit-art { position: absolute; left: 6px; top: 578px; width: 392px; height: 392px; border-radius: 50%;
    background: radial-gradient(circle at 60% 52%, #7a4b27 0 22%, #c89a78 30%, #fbe3d3 48%, #fff5ee 62%, var(--white) 72%); }

  .volume { position: absolute; left: 0; right: 0; bottom: 30px; text-align: center;
    font-family: "Arimo", Arial, sans-serif; font-size: 27px; color: var(--ink); }

  .back-strip { position: absolute; right: 0; top: 0; width: 46px; height: 1200px; background: var(--sand); }
  .info-box { position: absolute; left: 573px; top: 956px; width: 263px; height: 152px;
    border: 2px solid var(--ink); background: var(--white); }
</style>
</head>
<body>
<div class="label">
  <section class="front-panel" role="img" aria-label="Soft sand background with a scattered outline star pattern"></section>
  <div class="front-card">
    <div class="front-inner">
      <div class="brand">
        <span class="brand-dot"></span>
        <span class="brand-name">Pebble Lane<br>Naturals</span>
      </div>
      <div class="brand-rule"></div>
      <p class="tagline">Organic and Natural<br>Skin Care Products</p>

      <p class="range">Baby Organic</p>
      <div class="flavour-band"></div>
      <p class="flavour">Coconut</p>
      <p class="product">body lotion</p>

      <div class="fruit-art" role="img" aria-label="Illustration of a whole coconut and a split coconut half inside a soft peach brush-stroke circle"></div>

      <p class="volume">50 ml</p>
    </div>
  </div>
  <div class="info-box"></div>
  <div class="back-strip"></div>
</div>
</body>
</html>
```